Meadowlark Learning Growth Partners (MLGP)

This is a professional business card. Logo and picture are a must on the front of the card. I am an educational consultant. I have been consulting for the past three years for a company. I am now opening my own company. My goal for my consulting company is to eventually consult all over America.

Target Market(s)

Educators, schools, professionals

Industry/Entity Type

Consulting

Contact Information for Business Card

Picture/logo on front, simple modern design

Font styles to use
Serif

Colors
85abd2
0355a3
3176b5
cedeed

Requirements
Must have
• picture, logo,
• Odessa Pruitt, Ed.S
• address 5073 Cormorant ridge Dr. Nashville, TN 37940
• Cell:616-555-0148
• Office: 629-555-0172
• www.Mlgpedu.example
• pruittodessa@mailbox.example

```html
<!DOCTYPE html>
<html lang="en">
<head>
<meta charset="UTF-8">
<title>MLGP Business Card</title>
<link rel="stylesheet" href="https://fonts.googleapis.com/css2?family=Source+Sans+3:wght@400;600;700&display=swap">
<style>
  :root {
    --navy: #0a3a82;
    --blue: #0355a3;
    --mid-blue: #3176b5;
    --soft-blue: #85abd2;
    --pale-blue: #cedeed;
    --ink: #1b1b1b;
    --paper: #ffffff;
    --backdrop: #2b2b2d;
  }
  * { margin: 0; padding: 0; box-sizing: border-box; }
  html, body { width: 1200px; height: 1000px; overflow: hidden; }
  body {
    position: relative;
    background: var(--backdrop);
    font-family: "Source Sans 3", sans-serif;
    color: var(--navy);
  }
  .card {
    position: absolute;
    width: 657px;
    height: 374px;
    background: var(--paper);
    border-radius: 40px;
    overflow: hidden;
  }
  .card-back { left: 137px; top: 77px; }
  .card-front { left: 401px; top: 534px; }

  /* Back: brand lockup */
  .brand-mark {
    position: absolute;
    left: 50%;
    top: 92px;
    transform: translateX(-50%);
    display: flex;
    flex-direction: column;
    align-items: center;
    gap: 18px;
  }
  .brand-dot {
    width: 92px; height: 92px;
    border-radius: 50%;
    background: var(--blue);
  }
  .brand-name-large {
    font-weight: 700;
    font-size: 60px;
    letter-spacing: 5px;
    line-height: 1;
    color: var(--navy);
  }

  /* Front */
  .front-art { position: absolute; inset: 0; }
  .header {
    position: absolute;
    left: 36px; top: 28px;
    display: flex;
    align-items: center;
  }
  .header-square {
    width: 58px; height: 58px;
    background: var(--blue);
    margin-right: 12px;
  }
  .header-name {
    font-weight: 700;
    font-size: 27px;
    letter-spacing: 2px;
    color: var(--navy);
    padding-right: 12px;
  }
  .header-divider {
    width: 1.5px; height: 68px;
    background: var(--navy);
    margin-right: 8px;
  }
  .header-full {
    font-weight: 700;
    font-size: 13.5px;
    line-height: 17px;
    color: var(--navy);
  }
  .person-name {
    position: absolute;
    left: 34px; top: 130px;
    font-size: 29px;
    font-weight: 400;
    color: var(--navy);
  }
  .person-title {
    position: absolute;
    left: 35px; top: 170px;
    font-size: 19px;
    color: var(--navy);
  }
  .contact-list {
    position: absolute;
    left: 34px; top: 224px;
    list-style: none;
  }
  .contact-list li {
    display: flex;
    align-items: center;
    height: 30.5px;
    font-size: 19px;
    color: var(--navy);
  }
  .contact-list svg { width: 18px; height: 18px; margin-right: 15px; fill: var(--mid-blue); }
  .address {
    position: absolute;
    left: 31px; top: 329px;
    font-size: 16.5px;
    color: var(--ink);
  }
  .website {
    position: absolute;
    right: 37px; top: 327px;
    font-size: 18.5px;
    color: var(--blue);
  }
</style>
</head>
<body>

<section class="card card-back">
  <div class="brand-mark">
    <div class="brand-dot"></div>
    <div class="brand-name-large">MLGP</div>
  </div>
</section>

<section class="card card-front">
  <svg class="front-art" viewBox="0 0 657 374" width="657" height="374">
    <defs>
      <linearGradient id="portraitTone" x1="0" y1="0" x2="0" y2="1">
        <stop offset="0" stop-color="#e9e4de"/>
        <stop offset="0.45" stop-color="#d8c6ad"/>
        <stop offset="1" stop-color="#23283a"/>
      </linearGradient>
    </defs>
    <rect x="437" y="20" width="220" height="275" fill="url(#portraitTone)" role="img" aria-label="Portrait photo of Odessa Pruitt"/>
    <path d="M0,240 C60,205 100,192 140,194 C230,196 320,268 400,268 C500,268 590,245 657,228 L657,374 L0,374 Z" fill="#ffffff"/>
    <path d="M0,240 C60,205 100,192 140,194 C230,196 320,268 400,268" fill="none" stroke="#0a3a82" stroke-width="1.6"/>
    <path d="M250,232 C320,262 360,268 400,268 C500,268 590,245 657,228 L657,250 C590,274 500,290 400,289 C340,288 295,262 250,232 Z" fill="#0a3a82"/>
  </svg>

  <div class="header">
    <div class="header-square"></div>
    <div class="header-name">MLGP</div>
    <div class="header-divider"></div>
    <div class="header-full">Meadowlark<br>Learning<br>Growth<br>Partners</div>
  </div>

  <h1 class="person-name">Odessa Pruitt</h1>
  <p class="person-title">Ed.S</p>

  <ul class="contact-list">
    <li>
      <svg viewBox="0 0 24 24"><path d="M12 1a11 11 0 1 0 0 22 11 11 0 0 0 0-22zm0 2a9 9 0 1 1 0 18 9 9 0 0 1 0-18zM8.6 6.5c-.5 0-1.5.6-1.5 1.9 0 3.6 4.9 8.9 8.6 9 1.3 0 1.9-1 1.9-1.5l-.2-.6-2.1-1.1-.6.1-.9 1c-1.5-.6-3.4-2.5-4-4l1-.9.1-.6-1.1-2.1z"/></svg>
      616-555-0148
    </li>
    <li>
      <svg viewBox="0 0 24 24"><path d="M2 8c0-2 4-4 10-4s10 2 10 4v2h-5V8c-1-.6-3-1-5-1s-4 .4-5 1v2H2zM6 11l2-2h8l2 2 2 9H4zm6 1.5a3 3 0 1 0 0 6 3 3 0 0 0 0-6z"/></svg>
      629-555-0172
    </li>
    <li>
      <svg viewBox="0 0 24 24"><path d="M2 5h20v14H2zm2 2v.4l8 5.6 8-5.6V7zm0 2.8V17h16V9.8l-8 5.6z"/></svg>
      pruittodessa@mailbox.example
    </li>
  </ul>

  <p class="address">5073 Cormorant ridge Dr. Nashville, TN 37940</p>
  <p class="website">www.Mlgpedu.example</p>
</section>

</body>
</html>
```